Restaurant table menu

I need to design restaurants table menu. I wanted to have menu with pictures. Our current website has menu with pictures and need to translate that in paper for table menu. http://belmoravi.shop/. I want clean simple and elegant.
Link to logo. Use what don't and color do you think is best. At least need to see one page done completely for sample

https://files.quorvex.com/folderview?id=8RtPmWzq3LdNcYe5HvJaKoGsXbTiFuMnQ

```html
<!DOCTYPE html>
<html lang="en">
<head>
<meta charset="utf-8">
<title>Belmoravi Indian Cuisine – Table Menu</title>
<link rel="stylesheet" href="https://fonts.googleapis.com/css2?family=Montserrat:wght@500;600;700;800&family=Open+Sans:wght@400;600&display=swap">
<style>
  :root{
    --menu-red:#a3232c;
    --menu-red-deep:#7c1820;
    --menu-red-soft:#c0353c;
    --menu-gold:#f0b94a;
    --paper:#ffffff;
    --ink:#3a3a3a;
    --muted:#6d6d6d;
    --stage:#ece6df;
    --photo-a:#b0672e;
    --photo-b:#6f3a1c;
  }
  *{box-sizing:border-box;margin:0;padding:0}
  html,body{width:1200px;height:801px;overflow:hidden}
  body{background:var(--stage);font-family:"Open Sans",Arial,sans-serif;color:var(--ink);position:relative}
  ul{list-style:none}

  .sheet{position:absolute;top:110px;width:560px;height:580px;display:grid;grid-template-columns:1fr 1fr;background:var(--paper);box-shadow:0 4px 14px rgba(0,0,0,.18)}
  .sheet--inside{left:30px;border:5px solid var(--menu-red)}
  .sheet--outside{left:610px}

  .panel{padding:10px 8px;position:relative;min-width:0}
  .column{min-width:0}
  .panel--starters{display:grid;grid-template-columns:30px 1fr 1fr;gap:6px;border-right:1px solid #e2d6d6}
  .panel--mains{display:grid;grid-template-columns:1fr 1fr;gap:8px;padding:10px 6px}
  .panel--rice{display:grid;grid-template-columns:1fr 1fr;gap:10px;border:5px solid var(--menu-red);border-right:none}

  .menu-title{writing-mode:vertical-rl;transform:rotate(180deg);font-family:"Montserrat",sans-serif;font-weight:800;font-size:22px;color:var(--menu-red);letter-spacing:2px;text-align:right}

  .section-head{font-family:"Montserrat",sans-serif;font-weight:700;font-size:7.5px;color:#fff;background:var(--menu-red);padding:2px 5px;margin:3px 0 4px;display:inline-block;letter-spacing:.5px}

  .dish{display:flex;align-items:flex-start;gap:3px;margin-bottom:3px;min-height:22px}
  .dish-text{flex:1;min-width:0}
  .dish-name{font-family:"Montserrat",sans-serif;font-weight:700;font-size:6px;color:var(--menu-red);display:flex;justify-content:space-between;gap:3px;line-height:1.25;white-space:nowrap}
  .dish-price{color:var(--ink);font-weight:600}
  .dish-desc{font-size:5.2px;line-height:1.3;color:var(--muted)}
  .dish-photo{width:11px;height:11px;flex:none;border:1px solid var(--menu-red);background:linear-gradient(135deg,var(--photo-a),var(--photo-b))}

  .dish--compact{min-height:0;margin-bottom:5px;align-items:center}
  .dish--compact .dish-name{font-size:6px}
  .dish--compact .dish-photo{width:10px;height:10px}

  .panel--cover{background:linear-gradient(160deg,var(--menu-red-soft),var(--menu-red-deep));color:#fff;padding:16px 14px;display:flex;flex-direction:column}
  .brand{display:flex;align-items:center;gap:6px}
  .brand-mark{width:9px;height:9px;border-radius:50%;background:var(--menu-gold)}
  .brand-name{font-family:"Montserrat",sans-serif;font-weight:700;font-size:13px;color:var(--menu-gold)}
  .brand-tagline{font-size:6.5px;margin:2px 0 0 15px;opacity:.9}
  .cover-title{font-family:"Montserrat",sans-serif;font-weight:800;font-size:28px;letter-spacing:2px;text-align:right;margin-top:26px}
  .cover-art{position:relative;height:250px;margin:10px -14px 0}
  .cover-art svg{position:absolute;inset:0;width:100%;height:100%}
  .cover-photo{position:absolute;left:14px;right:40px;top:30px;bottom:30px;border-radius:0 110px 110px 0;background:radial-gradient(circle at 40% 45%,#d48a3a,#8a4a20 60%,#4a2412)}
  .cover-contact{margin-top:auto;display:flex;justify-content:space-between;gap:8px;font-size:6.5px;line-height:1.45}
  .contact-label{font-family:"Montserrat",sans-serif;font-weight:700;font-size:8px;letter-spacing:.5px}
  .contact-phone{font-family:"Montserrat",sans-serif;font-weight:800;font-size:17px;color:var(--menu-gold)}
  .contact-block--call{text-align:right}
</style>
</head>
<body>

<section class="sheet sheet--inside" aria-label="Inside of table menu">
  <div class="panel panel--starters">
    <h1 class="menu-title">MENU</h1>
    <div class="column">
      <h3 class="section-head">APPETIZERS</h3>
      <ul>
        <li class="dish dish--compact"><div class="dish-text"><p class="dish-name">SAMOSA <span class="dish-price">$4.95</span></p></div><span class="dish-photo" role="img" aria-label="Samosa photo"></span></li>
        <li class="dish dish--compact"><div class="dish-text"><p class="dish-name">VEG PAKORA <span class="dish-price">$5.00</span></p></div><span class="dish-photo" role="img" aria-label="Pakora photo"></span></li>
        <li class="dish dish--compact"><div class="dish-text"><p class="dish-name">ONION BHAJI <span class="dish-price">$5.00</span></p></div><span class="dish-photo" role="img" aria-label="Onion bhaji photo"></span></li>
        <li class="dish dish--compact"><div class="dish-text"><p class="dish-name">ALOO TIKKI <span class="dish-price">$5.00</span></p></div><span class="dish-photo" role="img" aria-label="Aloo tikki photo"></span></li>
        <li class="dish dish--compact"><div class="dish-text"><p class="dish-name">PAPRI CHAAT <span class="dish-price">$5.95</span></p></div><span class="dish-photo" role="img" aria-label="Chaat photo"></span></li>
        <li class="dish dish--compact"><div class="dish-text"><p class="dish-name">FISH PAKORA <span class="dish-price">$6.95</span></p></div><span class="dish-photo" role="img" aria-label="Fish pakora photo"></span></li>
        <li class="dish dish--compact"><div class="dish-text"><p class="dish-name">CHILLI WINGS <span class="dish-price">$6.95</span></p></div><span class="dish-photo" role="img" aria-label="Chicken wings photo"></span></li>
      </ul>
      <h3 class="section-head">SOUPS</h3>
      <ul>
        <li class="dish dish--compact"><div class="dish-text"><p class="dish-name">DAL SOUP <span class="dish-price">$3.95</span></p></div><span class="dish-photo" role="img" aria-label="Lentil soup photo"></span></li>
        <li class="dish dish--compact"><div class="dish-text"><p class="dish-name">TOMATO SOUP <span class="dish-price">$3.95</span></p></div><span class="dish-photo" role="img" aria-label="Tomato soup photo"></span></li>
        <li class="dish dish--compact"><div class="dish-text"><p class="dish-name">MULLIGATAWNY <span class="dish-price">$4.50</span></p></div><span class="dish-photo" role="img" aria-label="Mulligatawny soup photo"></span></li>
      </ul>
      <h3 class="section-head">SALADS</h3>
      <ul>
        <li class="dish dish--compact"><div class="dish-text"><p class="dish-name">GARDEN SALAD <span class="dish-price">$4.00</span></p></div><span class="dish-photo" role="img" aria-label="Garden salad photo"></span></li>
        <li class="dish dish--compact"><div class="dish-text"><p class="dish-name">KACHUMBER <span class="dish-price">$4.00</span></p></div><span class="dish-photo" role="img" aria-label="Kachumber salad photo"></span></li>
      </ul>
    </div>
    <div class="column">
      <h3 class="section-head">TANDOORI</h3>
      <ul>
        <li class="dish dish--compact"><div class="dish-text"><p class="dish-name">TANDOORI WINGS <span class="dish-price">$9.00</span></p></div><span class="dish-photo" role="img" aria-label="Tandoori wings photo"></span></li>
        <li class="dish dish--compact"><div class="dish-text"><p class="dish-name">SEEKH KABAB <span class="dish-price">$9.00</span></p></div><span class="dish-photo" role="img" aria-label="Seekh kabab photo"></span></li>
        <li class="dish dish--compact"><div class="dish-text"><p class="dish-name">MALAI TIKKA <span class="dish-price">$9.00</span></p></div><span class="dish-photo" role="img" aria-label="Malai tikka photo"></span></li>
        <li class="dish dish--compact"><div class="dish-text"><p class="dish-name">PANEER TIKKA <span class="dish-price">$9.00</span></p></div><span class="dish-photo" role="img" aria-label="Paneer tikka photo"></span></li>
        <li class="dish dish--compact"><div class="dish-text"><p class="dish-name">HARA KABAB <span class="dish-price">$8.00</span></p></div><span class="dish-photo" role="img" aria-label="Hara kabab photo"></span></li>
      </ul>
      <h3 class="section-head">BREADS</h3>
      <ul>
        <li class="dish dish--compact"><div class="dish-text"><p class="dish-name">PLAIN NAAN <span class="dish-price">$2.50</span></p></div><span class="dish-photo" role="img" aria-label="Naan photo"></span></li>
        <li class="dish dish--compact"><div class="dish-text"><p class="dish-name">GARLIC NAAN <span class="dish-price">$3.00</span></p></div><span class="dish-photo" role="img" aria-label="Garlic naan photo"></span></li>
        <li class="dish dish--compact"><div class="dish-text"><p class="dish-name">ROTI <span class="dish-price">$2.50</span></p></div><span class="dish-photo" role="img" aria-label="Roti photo"></span></li>
        <li class="dish dish--compact"><div class="dish-text"><p class="dish-name">ONION KULCHA <span class="dish-price">$3.50</span></p></div><span class="dish-photo" role="img" aria-label="Kulcha photo"></span></li>
        <li class="dish dish--compact"><div class="dish-text"><p class="dish-name">ALOO PARATHA <span class="dish-price">$3.95</span></p></div><span class="dish-photo" role="img" aria-label="Paratha photo"></span></li>
      </ul>
      <h3 class="section-head">DESSERTS</h3>
      <ul>
        <li class="dish dish--compact"><div class="dish-text"><p class="dish-name">GULAB JAMUN <span class="dish-price">$3.50</span></p></div><span class="dish-photo" role="img" aria-label="Gulab jamun photo"></span></li>
        <li class="dish dish--compact"><div class="dish-text"><p class="dish-name">KHEER <span class="dish-price">$3.50</span></p></div><span class="dish-photo" role="img" aria-label="Rice pudding photo"></span></li>
      </ul>
    </div>
  </div>

  <div class="panel panel--mains">
    <div class="column">
      <ul>
        <li class="dish"><div class="dish-text"><p class="dish-name">PURI <span class="dish-price">$4.95</span></p><p class="dish-desc">Onions and fresh herbs mixed with gram flour and deep fried</p></div><span class="dish-photo" role="img" aria-label="Puri photo"></span></li>
        <li class="dish"><div class="dish-text"><p class="dish-name">PISWARI NAAN <span class="dish-price">$9.00</span></p><p class="dish-desc">Comes with vegetable korma, chicken curry, Naan, rice, and dessert</p></div><span class="dish-photo" role="img" aria-label="Peshwari naan photo"></span></li>
        <li class="dish"><div class="dish-text"><p class="dish-name">PANEER NAAN <span class="dish-price">$9.00</span></p><p class="dish-desc">Comes with vegetable korma, chicken curry, Naan, rice, and dessert</p></div><span class="dish-photo" role="img" aria-label="Paneer naan photo"></span></li>
        <li class="dish"><div class="dish-text"><p class="dish-name">BREAD BASKET <span class="dish-price">$3.00</span></p><p class="dish-desc">Comes with vegetable korma, chicken curry, Naan, rice, and dessert</p></div><span class="dish-photo" role="img" aria-label="Bread basket photo"></span></li>
      </ul>
      <h3 class="section-head">VEGETARIAN</h3>
      <ul>
        <li class="dish"><div class="dish-text"><p class="dish-name">VEGETABLE CURRY <span class="dish-price">$4.95</span></p><p class="dish-desc">Onions and fresh herbs mixed with gram flour and deep fried</p></div><span class="dish-photo" role="img" aria-label="Vegetable curry photo"></span></li>
        <li class="dish"><div class="dish-text"><p class="dish-name">VEGETABLE VINDALOO <span class="dish-price">$9.00</span></p><p class="dish-desc">Comes with vegetable korma, chicken curry, Naan, rice, and dessert</p></div><span class="dish-photo" role="img" aria-label="Vegetable vindaloo photo"></span></li>
        <li class="dish"><div class="dish-text"><p class="dish-name">VEGETABLE KORMA <span class="dish-price">$9.00</span></p><p class="dish-desc">Comes with vegetable korma, chicken curry, Naan, rice, and dessert</p></div><span class="dish-photo" role="img" aria-label="Vegetable korma photo"></span></li>
        <li class="dish"><div class="dish-text"><p class="dish-name">PANEER BHURJEE <span class="dish-price">$9.00</span></p><p class="dish-desc">Comes with vegetable korma, chicken curry, Naan, rice, and dessert</p></div><span class="dish-photo" role="img" aria-label="Paneer bhurjee photo"></span></li>
        <li class="dish"><div class="dish-text"><p class="dish-name">PANEER MAKHANI <span class="dish-price">$9.00</span></p><p class="dish-desc">Comes with vegetable korma, chicken curry, Naan, rice, and dessert</p></div><span class="dish-photo" role="img" aria-label="Paneer makhani photo"></span></li>
        <li class="dish"><div class="dish-text"><p class="dish-name">PANEER JHAL FRAIZEE <span class="dish-price">$9.00</span></p><p class="dish-desc">Comes with vegetable korma, chicken curry, Naan, rice, and dessert</p></div><span class="dish-photo" role="img" aria-label="Paneer jhal frazee photo"></span></li>
        <li class="dish"><div class="dish-text"><p class="dish-name">PANEER CHILLY FRY <span class="dish-price">$9.00</span></p><p class="dish-desc">Comes with vegetable korma, chicken curry, Naan, rice, and dessert</p></div><span class="dish-photo" role="img" aria-label="Paneer chilli fry photo"></span></li>
        <li class="dish"><div class="dish-text"><p class="dish-name">KATHMANDU PANEER <span class="dish-price">$9.00</span></p><p class="dish-desc">Comes with vegetable korma, chicken curry, Naan, rice, and dessert</p></div><span class="dish-photo" role="img" aria-label="Kathmandu paneer photo"></span></li>
        <li class="dish"><div class="dish-text"><p class="dish-name">SHAHI PANEER <span class="dish-price">$9.00</span></p><p class="dish-desc">Comes with vegetable korma, chicken curry, Naan, rice, and dessert</p></div><span class="dish-photo" role="img" aria-label="Shahi paneer photo"></span></li>
        <li class="dish"><div class="dish-text"><p class="dish-name">SAG PANEER <span class="dish-price">$9.00</span></p><p class="dish-desc">Comes with vegetable korma, chicken curry, Naan, rice, and dessert</p></div><span class="dish-photo" role="img" aria-label="Sag paneer photo"></span></li>
        <li class="dish"><div class="dish-text"><p class="dish-name">MUSHROOM MATAR <span class="dish-price">$9.00</span></p><p class="dish-desc">Comes with vegetable korma, chicken curry, Naan, rice, and dessert</p></div><span class="dish-photo" role="img" aria-label="Mushroom matar photo"></span></li>
        <li class="dish"><div class="dish-text"><p class="dish-name">MATAR ALU <span class="dish-price">$9.00</span></p><p class="dish-desc">Comes with vegetable korma, chicken curry, Naan, rice, and dessert</p></div><span class="dish-photo" role="img" aria-label="Matar aloo photo"></span></li>
        <li class="dish"><div class="dish-text"><p class="dish-name">MATAR PANEER <span class="dish-price">$3.99</span></p><p class="dish-desc">Comes with vegetable korma, chicken curry, Naan, rice, and dessert</p></div><span class="dish-photo" role="img" aria-label="Matar paneer photo"></span></li>
      </ul>
    </div>
    <div class="column">
      <h3 class="section-head">CHICKEN</h3>
      <ul>
        <li class="dish"><div class="dish-text"><p class="dish-name">CHICKEN CURRY <span class="dish-price">$4.95</span></p><p class="dish-desc">Onions and fresh herbs mixed with gram flour and deep fried</p></div><span class="dish-photo" role="img" aria-label="Chicken curry photo"></span></li>
        <li class="dish"><div class="dish-text"><p class="dish-name">CHICKEN DO PIAZZA <span class="dish-price">$9.00</span></p><p class="dish-desc">Comes with vegetable korma, chicken curry, Naan, rice, and dessert</p></div><span class="dish-photo" role="img" aria-label="Chicken do piaza photo"></span></li>
        <li class="dish"><div class="dish-text"><p class="dish-name">CHICKEN VEGETABLES <span class="dish-price">$9.00</span></p><p class="dish-desc">Comes with vegetable korma, chicken curry, Naan, rice, and dessert</p></div><span class="dish-photo" role="img" aria-label="Chicken with vegetables photo"></span></li>
        <li class="dish"><div class="dish-text"><p class="dish-name">KARHAI TANDOORI SAG <span class="dish-price">$9.00</span></p><p class="dish-desc">Comes with vegetable korma, chicken curry, Naan, rice, and dessert</p></div><span class="dish-photo" role="img" aria-label="Karahi tandoori chicken sag photo"></span></li>
        <li class="dish"><div class="dish-text"><p class="dish-name">BUTTER CHICKEN <span class="dish-price">$9.00</span></p><p class="dish-desc">Comes with vegetable korma, chicken curry, Naan, rice, and dessert</p></div><span class="dish-photo" role="img" aria-label="Butter chicken photo"></span></li>
        <li class="dish"><div class="dish-text"><p class="dish-name">CHICKEN TIKKA MUGHLAI <span class="dish-price">$9.00</span></p><p class="dish-desc">Comes with vegetable korma, chicken curry, Naan, rice, and dessert</p></div><span class="dish-photo" role="img" aria-label="Chicken tikka mughlai photo"></span></li>
        <li class="dish"><div class="dish-text"><p class="dish-name">CHICKEN METHI MALAI <span class="dish-price">$3.99</span></p><p class="dish-desc">Comes with vegetable korma, chicken curry, Naan, rice, and dessert</p></div><span class="dish-photo" role="img" aria-label="Chicken methi malai photo"></span></li>
      </ul>
      <h3 class="section-head">LAMB</h3>
      <ul>
        <li class="dish"><div class="dish-text"><p class="dish-name">LAMB KORMA <span class="dish-price">$4.95</span></p><p class="dish-desc">Onions and fresh herbs mixed with gram flour and deep fried</p></div><span class="dish-photo" role="img" aria-label="Lamb korma photo"></span></li>
        <li class="dish"><div class="dish-text"><p class="dish-name">LAMB TIKKA MASALA <span class="dish-price">$9.00</span></p><p class="dish-desc">Comes with vegetable korma, chicken curry, Naan, rice, and dessert</p></div><span class="dish-photo" role="img" aria-label="Lamb tikka masala photo"></span></li>
        <li class="dish"><div class="dish-text"><p class="dish-name">LAMB VINDALOO <span class="dish-price">$9.00</span></p><p class="dish-desc">Comes with vegetable korma, chicken curry, Naan, rice, and dessert</p></div><span class="dish-photo" role="img" aria-label="Lamb vindaloo photo"></span></li>
        <li class="dish"><div class="dish-text"><p class="dish-name">LAMB BHUNA <span class="dish-price">$9.00</span></p><p class="dish-desc">Comes with vegetable korma, chicken curry, Naan, rice, and dessert</p></div><span class="dish-photo" role="img" aria-label="Lamb bhuna photo"></span></li>
        <li class="dish"><div class="dish-text"><p class="dish-name">LAMB CURRY <span class="dish-price">$9.00</span></p><p class="dish-desc">Comes with vegetable korma, chicken curry, Naan, rice, and dessert</p></div><span class="dish-photo" role="img" aria-label="Lamb curry photo"></span></li>
        <li class="dish"><div class="dish-text"><p class="dish-name">LAMB ROGAN JOSH <span class="dish-price">$9.00</span></p><p class="dish-desc">Comes with vegetable korma, chicken curry, Naan, rice, and dessert</p></div><span class="dish-photo" role="img" aria-label="Lamb rogan josh photo"></span></li>
        <li class="dish"><div class="dish-text"><p class="dish-name">LAMB PASANDA <span class="dish-price">$3.99</span></p><p class="dish-desc">Comes with vegetable korma, chicken curry, Naan, rice, and dessert</p></div><span class="dish-photo" role="img" aria-label="Lamb pasanda photo"></span></li>
        <li class="dish"><div class="dish-text"><p class="dish-name">LAMB KARAHI <span class="dish-price">$9.00</span></p><p class="dish-desc">Comes with vegetable korma, chicken curry, Naan, rice, and dessert</p></div><span class="dish-photo" role="img" aria-label="Lamb karahi photo"></span></li>
        <li class="dish"><div class="dish-text"><p class="dish-name">LAMB MANGO <span class="dish-price">$9.00</span></p><p class="dish-desc">Comes with vegetable korma, chicken curry, Naan, rice, and dessert</p></div><span class="dish-photo" role="img" aria-label="Lamb mango curry photo"></span></li>
      </ul>
    </div>
  </div>
</section>

<section class="sheet sheet--outside" aria-label="Outside of table menu">
  <div class="panel panel--rice">
    <div class="column">
      <ul>
        <li class="dish dish--compact"><div class="dish-text"><p class="dish-name">LAMB SAAG <span class="dish-price">$9.00</span></p></div><span class="dish-photo" role="img" aria-label="Lamb saag photo"></span></li>
        <li class="dish dish--compact"><div class="dish-text"><p class="dish-name">LAMB MAKHANI <span class="dish-price">$9.00</span></p></div><span class="dish-photo" role="img" aria-label="Lamb makhani photo"></span></li>
        <li class="dish dish--compact"><div class="dish-text"><p class="dish-name">LAMB METHI <span class="dish-price">$9.00</span></p></div><span class="dish-photo" role="img" aria-label="Lamb methi photo"></span></li>
        <li class="dish dish--compact"><div class="dish-text"><p class="dish-name">LAMB CHILLI FRY <span class="dish-price">$9.00</span></p></div><span class="dish-photo" role="img" aria-label="Lamb chilli fry photo"></span></li>
        <li class="dish dish--compact"><div class="dish-text"><p class="dish-name">LAMB DO PIAZZA <span class="dish-price">$9.00</span></p></div><span class="dish-photo" role="img" aria-label="Lamb do piaza photo"></span></li>
      </ul>
      <h3 class="section-head">SPECIAL RICE</h3>
      <ul>
        <li class="dish dish--compact"><div class="dish-text"><p class="dish-name">WHITE RICE <span class="dish-price">$2.50</span></p></div><span class="dish-photo" role="img" aria-label="White rice photo"></span></li>
        <li class="dish dish--compact"><div class="dish-text"><p class="dish-name">JEERA RICE <span class="dish-price">$3.50</span></p></div><span class="dish-photo" role="img" aria-label="Jeera rice photo"></span></li>
        <li class="dish dish--compact"><div class="dish-text"><p class="dish-name">VEG FRIED RICE <span class="dish-price">$6.95</span></p></div><span class="dish-photo" role="img" aria-label="Vegetable fried rice photo"></span></li>
        <li class="dish dish--compact"><div class="dish-text"><p class="dish-name">CHICKEN FRIED RICE <span class="dish-price">$7.95</span></p></div><span class="dish-photo" role="img" aria-label="Chicken fried rice photo"></span></li>
        <li class="dish dish--compact"><div class="dish-text"><p class="dish-name">EGG FRIED RICE <span class="dish-price">$6.95</span></p></div><span class="dish-photo" role="img" aria-label="Egg fried rice photo"></span></li>
        <li class="dish dish--compact"><div class="dish-text"><p class="dish-name">MATAR PULAO <span class="dish-price">$5.95</span></p></div><span class="dish-photo" role="img" aria-label="Matar pulao photo"></span></li>
        <li class="dish dish--compact"><div class="dish-text"><p class="dish-name">VEG BIRYANI <span class="dish-price">$9.95</span></p></div><span class="dish-photo" role="img" aria-label="Vegetable biryani photo"></span></li>
        <li class="dish dish--compact"><div class="dish-text"><p class="dish-name">LAMB BIRYANI <span class="dish-price">$12.95</span></p></div><span class="dish-photo" role="img" aria-label="Lamb biryani photo"></span></li>
        <li class="dish dish--compact"><div class="dish-text"><p class="dish-name">SHRIMP BIRYANI <span class="dish-price">$12.95</span></p></div><span class="dish-photo" role="img" aria-label="Shrimp biryani photo"></span></li>
        <li class="dish dish--compact"><div class="dish-text"><p class="dish-name">CHICKEN BIRYANI <span class="dish-price">$10.95</span></p></div><span class="dish-photo" role="img" aria-label="Chicken biryani photo"></span></li>
      </ul>
    </div>
    <div class="column">
      <h3 class="section-head">SEAFOOD</h3>
      <ul>
        <li class="dish dish--compact"><div class="dish-text"><p class="dish-name">FISH CURRY <span class="dish-price">$12.95</span></p></div><span class="dish-photo" role="img" aria-label="Fish curry photo"></span></li>
        <li class="dish dish--compact"><div class="dish-text"><p class="dish-name">FISH MASALA <span class="dish-price">$12.95</span></p></div><span class="dish-photo" role="img" aria-label="Fish masala photo"></span></li>
        <li class="dish dish--compact"><div class="dish-text"><p class="dish-name">SHRIMP CURRY <span class="dish-price">$13.95</span></p></div><span class="dish-photo" role="img" aria-label="Shrimp curry photo"></span></li>
        <li class="dish dish--compact"><div class="dish-text"><p class="dish-name">SHRIMP KORMA <span class="dish-price">$13.95</span></p></div><span class="dish-photo" role="img" aria-label="Shrimp korma photo"></span></li>
        <li class="dish dish--compact"><div class="dish-text"><p class="dish-name">SHRIMP VINDALOO <span class="dish-price">$13.95</span></p></div><span class="dish-photo" role="img" aria-label="Shrimp vindaloo photo"></span></li>
      </ul>
      <h3 class="section-head">FROM THE TANDOOR</h3>
      <ul>
        <li class="dish dish--compact"><div class="dish-text"><p class="dish-name">TANDOORI CHICKEN <span class="dish-price">$11.95</span></p></div><span class="dish-photo" role="img" aria-label="Tandoori chicken photo"></span></li>
        <li class="dish dish--compact"><div class="dish-text"><p class="dish-name">CHICKEN TIKKA <span class="dish-price">$11.95</span></p></div><span class="dish-photo" role="img" aria-label="Chicken tikka photo"></span></li>
        <li class="dish dish--compact"><div class="dish-text"><p class="dish-name">TANDOORI FISH <span class="dish-price">$13.95</span></p></div><span class="dish-photo" role="img" aria-label="Tandoori fish photo"></span></li>
        <li class="dish dish--compact"><div class="dish-text"><p class="dish-name">TANDOORI SHRIMP <span class="dish-price">$14.95</span></p></div><span class="dish-photo" role="img" aria-label="Tandoori shrimp photo"></span></li>
        <li class="dish dish--compact"><div class="dish-text"><p class="dish-name">MIXED GRILL <span class="dish-price">$15.95</span></p></div><span class="dish-photo" role="img" aria-label="Mixed grill photo"></span></li>
        <li class="dish dish--compact"><div class="dish-text"><p class="dish-name">FISH TIKKA <span class="dish-price">$12.95</span></p></div><span class="dish-photo" role="img" aria-label="Fish tikka photo"></span></li>
        <li class="dish dish--compact"><div class="dish-text"><p class="dish-name">GOAN SHRIMP <span class="dish-price">$12.95</span></p></div><span class="dish-photo" role="img" aria-label="Goan shrimp photo"></span></li>
      </ul>
    </div>
  </div>

  <div class="panel panel--cover">
    <div class="brand">
      <span class="brand-mark"></span>
      <span class="brand-name">Belmoravi Indian Cuisine</span>
    </div>
    <p class="brand-tagline">An Authentic Indian Restaurant</p>
    <h2 class="cover-title">MENU</h2>
    <div class="cover-art">
      <div class="cover-photo" role="img" aria-label="Photo of an assortment of Indian curries in bowls"></div>
      <svg viewBox="0 0 285 250" preserveAspectRatio="none" aria-hidden="true">
        <path d="M0 222 C110 236 200 214 285 150 L285 168 C200 230 110 248 0 240 Z" fill="var(--menu-gold)"/>
        <path d="M150 18 C210 30 250 70 260 120" stroke="var(--menu-gold)" stroke-width="3" fill="none"/>
      </svg>
    </div>
    <div class="cover-contact">
      <div class="contact-block">
        <p class="contact-label">ORDER ONLINE</p>
        <p>orders@belmoravi.shop</p>
        <p>http://belmoravi.shop/</p>
      </div>
      <div class="contact-block contact-block--call">
        <p class="contact-label">CALL FOR DELIVERY</p>
        <p class="contact-phone">418-2790</p>
        <p>782 Larkfield Ave, Suite 12</p>
        <p>Dunmore, OH 44120</p>
      </div>
    </div>
  </div>
</section>

</body>
</html>
```